Custom Manufacturing Job Shop

We are looking for a business card design for Tall Oak Fabrication Inc. Tall Oak is a family owned business that manufactures any custom product to fit a customers needs, whether it is custom 1 piece or production parts, we truly take on projects that others just cant do. to help in your design go to www.talloakfab.example for a more in depth idea. we have the following capabilities that we would like to see on the card somewhere...maybe on the back of a 2 sided card? we are fully open to ideas.
Machining
• Fabrication
• Millwork
• Maintenance
• Laser Cutting
• Precision Forming
Engineering
Blasting/Painting

No matter how big or small, We literally do it all

preferably black or darker cards but we don't mind to see some color if you see a better fit. we are interested in looking at anything that catches attention.
I have attached our logo, if it is needed in a different file type please let me know and I will send it to you if I can. maybe adding some type of drawing or dimensional lines would be something to add?? just throwing ideas out there....

Reason: I added one of our shredder designs and would like to see a few more cards if possible using this. any questions please don't hesitate to ask!!

Target Market(s)

anyone looking for design/manufacturing/machining whether it is custom 1 off parts or production.

Industry/Entity Type

Business

Contact Information for Business Card

preferably darker shades, but also not opposed to some color in the same sense....not too bright

Font styles to use
Serif
Sans Serif

Requirements
Must have
• Dell Marwick
• Direct:555-213-7790
• Cell:555-348-1162
• Fax: 555-907-4425
• 42 Quarry Lane
• Klingerstown, PA 00000
• I also would request having it in a format I can give to the company making the business cards to edit names/numbers etc. for the entire staff.
Nice to have
• drafting lines? we are open to almost anything....
Should not have
• exotic colors

```html
<!DOCTYPE html>
<html lang="en">
<head>
<meta charset="utf-8">
<title>Tall Oak Fabrication – Business Card</title>
<link href="https://fonts.googleapis.com/css2?family=Open+Sans:wght@400;600;700&display=swap" rel="stylesheet">
<style>
  :root {
    --backdrop: #e6e6e6;
    --paper: #f4f5f3;
    --blue: #2f6cc4;
    --blue-deep: #1d4f9e;
    --steel: #4a4c50;
    --steel-light: #8a8c90;
    --ink-blue: #2a5fb0;
    --white: #ffffff;
  }
  * { margin: 0; padding: 0; box-sizing: border-box; }
  html, body {
    width: 1200px; height: 418px; overflow: hidden;
    background: var(--backdrop);
    font-family: "Open Sans", Arial, sans-serif;
  }
  .stage { position: relative; width: 1200px; height: 418px; }
  .card {
    position: absolute; top: 73px; width: 465px; height: 264px;
    overflow: hidden; box-shadow: 0 2px 6px rgba(0,0,0,.25);
  }
  .card--front { left: 115px; background: var(--paper); }
  .card--back {
    left: 610px;
    background: linear-gradient(120deg, var(--blue) 0%, var(--blue-deep) 100%);
    color: var(--white);
  }
  .card__swoosh { position: absolute; inset: 0; }
  .brand {
    position: absolute; display: flex; align-items: center; gap: 8px;
    font-weight: 700; color: var(--steel); letter-spacing: .5px;
  }
  .brand__dot {
    width: 16px; height: 16px; border-radius: 50%; background: var(--steel-light);
  }
  .card--front .brand { left: 22px; top: 36px; font-size: 34px; }
  .card--back .brand { left: 190px; top: 132px; font-size: 30px; color: #d9dbde; }
  .card--back .brand__dot { background: #b9bcc1; }
  .person { position: absolute; left: 32px; top: 190px; }
  .person__name { font-size: 18px; font-weight: 700; color: var(--ink-blue); }
  .person__role { font-size: 11px; letter-spacing: 2px; color: var(--steel); margin-top: 2px; }
  .contact {
    position: absolute; right: 22px; top: 136px; text-align: right;
    color: var(--white); font-size: 11px; line-height: 19.5px;
  }
  .contact__name { font-size: 13px; font-weight: 700; margin-bottom: 2px; }
  .contact b { font-weight: 700; }
  .services { position: absolute; left: 40px; top: 50px; }
  .services__title { font-size: 21px; font-weight: 600; letter-spacing: .5px; margin-bottom: 10px; }
  .services__list { list-style: none; font-size: 11px; line-height: 24.5px; }
  .services__list li::before { content: "\2022"; margin-right: 5px; }
  .services__footer {
    position: absolute; left: 40px; top: 210px; font-size: 13px; font-weight: 600;
  }
</style>
</head>
<body>
<main class="stage">
  <section class="card card--front">
    <svg class="card__swoosh" width="465" height="264" viewBox="0 0 465 264">
      <path d="M335 0 C 290 40 262 150 255 264 L 268 264 C 276 150 300 45 350 0 Z" fill="#4a4c50"/>
      <path d="M352 0 C 300 50 278 160 274 264 L 465 264 L 465 0 Z" fill="url(#frontBlue)"/>
      <defs>
        <linearGradient id="frontBlue" x1="0" y1="0" x2="1" y2="1">
          <stop offset="0" stop-color="#3576cf"/>
          <stop offset="1" stop-color="#1d4f9e"/>
        </linearGradient>
      </defs>
    </svg>
    <div class="brand"><span class="brand__dot"></span>Tall Oak</div>
    <div class="person">
      <div class="person__name">YOUR NAME</div>
      <div class="person__role">DIRECTOR</div>
    </div>
    <div class="contact">
      <div class="contact__name">Dell Marwick</div>
      <div><b>Direct :</b> 555-213-7790</div>
      <div><b>Cell :</b> 555-348-1162</div>
      <div><b>Fax :</b> 555-907-4425</div>
      <div>42 Quarry Lane</div>
    </div>
  </section>

  <section class="card card--back">
    <div class="services">
      <h2 class="services__title">Machining</h2>
      <ul class="services__list">
        <li>Fabrication</li>
        <li>Millwork</li>
        <li>Maintenance</li>
        <li>Laser Cutting</li>
        <li>Precision Forming</li>
      </ul>
    </div>
    <div class="services__footer">Engineering Blasting/Painting</div>
    <div class="brand"><span class="brand__dot"></span>Tall Oak</div>
  </section>
</main>
</body>
</html>
```